Ranked amongst the Best Colleges and Programs

the size of the ad is Full Page, with bleed*
8”x 10.75" plus 0.25" bleed'
you have two choices for the tagline .. please chose what ever you think will allow you to make a better ad.
The instructions on the brief are in red
I am looking for a hight quality modern ad to place in local weekly publications that will stand out .
I would like a ad that people will look at and say i would like to see what this ad is all about.
I apprecate creative work.
the ad should not be very crowded and the text should be able to be read.
if you decide to use people in the ad .. (you don't have to ) then it should be a male dressed in white shirt in and sports jacket.. or if you would like you can use a vector and then use male or female people.
please leave one inch on the bottom for the footer

Target Market(s)

potential middle class students from 23-35 years of age

Industry/Entity Type

education

Requirements
Must have
• .the " 98% employment rate" should stand out in the ad.. but should not be the main part of the ad
Nice to have
• creative
Should not have
• Should not be a very busy or crowded ad.. i prefer pictures of men but should be .. in a business suit .. that looks professional- white shirt

```html
<!DOCTYPE html>
<html lang="en">
<head>
<meta charset="UTF-8">
<title>Get ahead faster in your career</title>
<link rel="stylesheet" href="https://fonts.googleapis.com/css2?family=Figtree:wght@400;500;600;700;800&display=swap">
<style>
  :root {
    --navy-deep: #010f2d;
    --navy: #03204f;
    --sky: #62b6fb;
    --cyan: #19e3f2;
    --gold: #f5b400;
    --white: #ffffff;
    --icon: #7f9fdf;
    --photo-light: #fbfbfb;
    --photo-shade: #e6e6e6;
  }
  * { margin: 0; padding: 0; box-sizing: border-box; }
  html, body { width: 900px; height: 1200px; overflow: hidden; }
  body { font-family: "Figtree", sans-serif; background: var(--sky); }
  .ad { position: relative; width: 900px; height: 1200px; overflow: hidden; background: var(--sky); }
  .backdrop, .portrait, .award-icon { position: absolute; display: block; }
  .backdrop { left: 0; top: 0; }
  .portrait { left: 0; top: 0; }
  .headline {
    position: absolute; left: 84px; top: 66px;
    color: var(--white); font-weight: 700; font-size: 71px; line-height: 70px; letter-spacing: -0.5px;
  }
  .subline {
    position: absolute; left: 85px; top: 242px;
    color: var(--cyan); font-weight: 500; font-size: 22px; line-height: 31px;
  }
  .stat { position: absolute; left: 84px; top: 322px; color: var(--gold); }
  .stat-value { display: block; font-weight: 800; font-size: 96px; line-height: 88px; letter-spacing: -2px; }
  .stat-label { display: block; margin-left: 11px; margin-top: 2px; font-weight: 600; font-size: 18.5px; letter-spacing: -0.2px; }
  .award-icon { left: 74px; top: 614px; }
  .rankings { position: absolute; left: 76px; top: 850px; color: var(--white); }
  .rankings-title { font-weight: 600; font-size: 27px; line-height: 40px; text-decoration: underline; text-underline-offset: 4px; text-decoration-thickness: 2px; }
  .rankings-list { list-style: none; font-weight: 500; font-size: 28px; line-height: 39px; }
  .rankings-list li { position: relative; padding-left: 30px; }
  .rankings-list li::before { content: ""; position: absolute; left: 0; top: 12px; border-left: 19px solid var(--white); border-top: 9px solid transparent; border-bottom: 9px solid transparent; }
  .rankings-list .source { display: block; padding-left: 6px; }
  .footnote {
    position: absolute; left: 79px; top: 1076px; width: 700px;
    color: var(--white); font-weight: 500; font-size: 15.6px; line-height: 24px;
  }
</style>
</head>
<body>
<main class="ad">
  <svg class="backdrop" width="900" height="1200" viewBox="0 0 900 1200" aria-hidden="true">
    <path d="M0 0 H868 L410 458 Q370 498 318 498 H0 Z" fill="var(--navy-deep)"/>
    <path d="M0 529 H180 Q240 529 280 569 L900 1189 V1200 H0 Z" fill="var(--navy)"/>
  </svg>

  <svg class="portrait" width="900" height="1200" viewBox="0 0 900 1200" role="img" aria-label="Portrait of a smiling bearded professional man in a crisp white shirt against a light wall">
    <defs>
      <linearGradient id="portrait-fill" x1="0" y1="0" x2="1" y2="1">
        <stop offset="0" stop-color="var(--photo-light)"/>
        <stop offset="1" stop-color="var(--photo-shade)"/>
      </linearGradient>
      <filter id="portrait-shadow" x="-20%" y="-20%" width="140%" height="140%">
        <feDropShadow dx="0" dy="6" stdDeviation="8" flood-color="#0a2a55" flood-opacity="0.35"/>
      </filter>
    </defs>
    <rect x="500" y="295" width="580" height="580" rx="72" transform="rotate(45 790 585)" fill="url(#portrait-fill)" filter="url(#portrait-shadow)"/>
  </svg>

  <h1 class="headline">Get ahead faster<br>in your career</h1>
  <p class="subline">With a prestigious KVU -<br>Masters of Accounting Degree.</p>

  <div class="stat">
    <span class="stat-value">98%</span>
    <span class="stat-label">EMPLOYMENT RATE</span>
  </div>

  <svg class="award-icon" width="126" height="176" viewBox="0 0 126 176" aria-hidden="true" fill="none" stroke="var(--icon)" stroke-width="3.5" stroke-linejoin="round" stroke-linecap="round">
    <path d="M63 4 L72 11 L83 8 L88 18 L99 20 L100 31 L109 38 L105 48 L110 58 L102 66 L103 77 L93 81 L89 92 L78 92 L70 100 L63 96 L56 100 L48 92 L37 92 L33 81 L23 77 L24 66 L16 58 L21 48 L17 38 L26 31 L27 20 L38 18 L43 8 L54 11 Z"/>
    <circle cx="63" cy="54" r="41"/>
    <path d="M63 30 L69.5 45 L85 46.5 L73 57 L77 72.5 L63 64.5 L49 72.5 L53 57 L41 46.5 L56.5 45 Z"/>
    <path d="M38 95 L8 158 L30 149 L38 172 L60 105"/>
    <path d="M88 95 L118 158 L96 149 L88 172 L66 105"/>
  </svg>

  <section class="rankings">
    <h2 class="rankings-title">Ranked amongst:</h2>
    <ul class="rankings-list">
      <li>Best Colleges-Meridian Review 2023</li>
      <li>Best Masters in Accounting Degree<span class="source">- GradScope 2023</span></li>
    </ul>
  </section>

  <p class="footnote">KVU graduates have gone on to work in various high-quality jobs in top firms, earning impressive six-figure salaries as well as opening successful businesses.</p>
</main>
</body>
</html>
```